Medical Internet Marketing Company Needs a Site!

We need a new, fresh website for our search engine optimization and social media marketing company. We specialize in helping medical practices, doctors, physicians, and hospitals with their online presence and web ranking. The site should lean towards being suited for these audiences.

We have several examples of website that we like as well as things that we like about them.

Here are sites that we enjoy.

www.brightwavelab.com

It's a good design for the site all around. The videos, buttons, and images are all excellent. They did a fine job.

- We really like their "contact us" side bar and want to include one like it on the secondary pages.

www.corvantis.net

- We don't like the "thickness" of the top navigation bar.
- We like the page colors, easy navigation, and big call to action phone number in the top right corner.

http://www.teluvo.com/

Out of all the examples provided, Teluvo is our favorite and closest look and style to what we are looking for.

- We really like the openness of the design, such as space between the text and background.

- We want a price page in a style very similar to their pricing page with the services listed and check-marks, etc. although we intend to have multiple service package columns much like Corvantis's SEO pricing page.

- The way the video fits into the home page header is very organized, simple, and attention grabbing. We intend to place a slider with videos here.

- We need a page design that will allow for an image slider like Teluvo's Features page.

Here's a great example of a medical internet marketing website: http://www.dermaplex.com/

Target Market(s)

Our target market is doctors, typically male and typically 40-45 years old. I

Industry/Entity Type

Marketing

Requirements
Must have
• The homepage should have a slider in the video. Interior pages should have a video in the very top similar to how they do it on www.brightwavelab.com

The top navigation tabs needed are:
- Home
- Solutions
- Resources
- About
- Why Quelvo
- Contact

The sidebar should have a GREAT call to action in it on interior pages.

There should be one interior page that is similar to this - http://www.teluvo.com/pricing/

There needs to be a page with multiple boxes that take up a row of the web page's body. This page will house all the case studies similar to brightwave lab's: http://www.brightwavelab.com/success-stories/case-studies/ The one exception is we want the case studies to be inside of "boxes" instead of between horizontal lines like brightwave lab's.
Nice to have
• Color, professional, and clean. GREAT use of calls to actions.

```html
<!DOCTYPE html>
<html lang="en">
<head>
<meta charset="utf-8">
<title>Quelvo – Medical Internet Marketing</title>
<link href="https://fonts.googleapis.com/css2?family=Ubuntu:wght@300;400;500;700&display=swap" rel="stylesheet">
<style>
:root{
  --header:#4d5561;
  --header-line:#ffffff;
  --nav-text:#ffffff;
  --logo-grey:#b9bdc3;
  --hero-top:#e9eff5;
  --hero-bottom:#b7cadc;
  --ink:#2f4a63;
  --body-text:#555b61;
  --page:#f4f4f4;
  --rule:#e2e2e2;
  --teal:#3aa88a;
  --slate:#3f4b58;
  --gold:#d8a21a;
  --btn-dark:#2d3640;
  --btn-gold:#e8ac1c;
  --footer:#3a3a3a;
  --footer-text:#e0e0e0;
  --footer-rule:#4a4a4a;
  --icon-dark:#333333;
}
*{box-sizing:border-box;margin:0;padding:0}
html,body{width:1062px;height:1200px;overflow:hidden;background:var(--page)}
body{position:relative;font-family:"Ubuntu",sans-serif;color:var(--body-text)}
.abs{position:absolute}

/* header */
.site-header{position:absolute;left:0;top:0;width:1062px;height:94px;background:var(--header);border-top:3px solid var(--header-line)}
.utility-tabs{position:absolute;left:768px;top:-3px;display:flex;gap:4px}
.utility-tabs span{display:block;background:#fff;color:#444;font-size:10px;height:17px;line-height:17px;padding:0 11px;border-radius:0 0 2px 2px}
.utility-tabs span:last-child{width:56px;text-align:center}
.brand{position:absolute;left:159px;top:33px;display:flex;align-items:center;gap:8px}
.brand-mark{width:20px;height:20px;background:var(--logo-grey)}
.brand-name{font-size:30px;font-weight:500;letter-spacing:3px;color:var(--logo-grey);line-height:1}
.main-nav{position:absolute;top:66px;left:0;width:1062px;height:14px}
.main-nav span{position:absolute;font-size:10.5px;color:var(--nav-text);letter-spacing:.2px}
.nav-pointer{position:absolute;left:498px;top:87px;width:0;height:0;border-left:4px solid transparent;border-right:4px solid transparent;border-bottom:7px solid var(--hero-top)}

/* hero */
.hero{position:absolute;left:0;top:94px;width:1062px;height:316px;background:linear-gradient(180deg,var(--hero-top) 0%,#d3dfea 60%,var(--hero-bottom) 100%)}
.hero-title{position:absolute;left:159px;top:40px;font-size:29px;font-weight:300;color:var(--ink);line-height:35px}
.hero-title b{font-weight:700}
.hero-copy{position:absolute;left:160px;top:148px;width:315px;font-size:12px;line-height:20.5px;font-weight:300;color:#3b4a58}
.btn{position:absolute;top:224px;height:41px;border-radius:3px;font-size:13.5px;line-height:41px;text-align:center;color:#fff;box-shadow:0 2px 3px rgba(0,0,0,.25)}
.btn-signup{left:161px;width:117px;background:linear-gradient(180deg,#46525e,var(--btn-dark))}
.btn-prices{left:284px;width:115px;background:linear-gradient(180deg,#f2bd3a,var(--btn-gold))}
.hero-screen{position:absolute;left:569px;top:30px;width:313px;height:252px;border-radius:6px;background:linear-gradient(180deg,#2a2a2a 0%,#2a2a2a 74%,#cfd2d5 74%,#9fa3a7 100%)}
.hero-screen .screen-photo{position:absolute;left:12px;top:13px;width:289px;height:164px;background:linear-gradient(90deg,#e6e2dc,#c9d8e6 60%,#dfe6ec)}

/* steps */
.steps-divider{position:absolute;left:414px;top:428px;width:1px;height:352px;background:var(--rule)}
.step{position:absolute;left:160px;width:230px}
.step-number{position:absolute;left:0;top:0;width:44px;height:44px;border-radius:50%;border:2px solid #fff;box-shadow:0 2px 4px rgba(0,0,0,.3);color:#fff;font-size:22px;font-weight:300;text-align:center;line-height:40px}
.step-title{position:absolute;left:56px;top:-2px;font-size:19.5px;font-weight:400;white-space:nowrap}
.step-sub{position:absolute;left:59px;top:21px;font-size:9.5px;white-space:nowrap}
.step-text{position:absolute;left:59px;top:39px;width:170px;font-size:9.5px;line-height:12px;font-weight:300}
.read-btn{position:absolute;font-size:8.5px;color:#333;background:#fff;border:1px solid #e3e3e3;padding:0 4px;height:16px;line-height:15px}
.step .read-btn{left:59px;top:72px}
.step-teal .step-number{background:var(--teal)} .step-teal .step-title,.step-teal .step-sub{color:var(--teal)}
.step-slate .step-number{background:var(--slate)} .step-slate .step-title,.step-slate .step-sub{color:#253340}
.step-gold .step-number{background:var(--gold)} .step-gold .step-title,.step-gold .step-sub{color:var(--gold)}
.step-rule{position:absolute;left:160px;width:230px;height:1px;background:var(--rule)}

/* welcome */
.welcome{position:absolute;left:440px;top:442px;width:463px}
.welcome h2{font-size:19px;font-weight:300;color:var(--ink);margin-bottom:9px}
.welcome h3{font-size:16px;font-weight:300;color:var(--ink);margin:14px 0 9px}
.welcome p{font-size:9.3px;line-height:11.8px;font-weight:300;text-align:justify;margin-bottom:11px}
.testimonial{font-size:9.3px;line-height:11.8px;font-weight:300;margin-bottom:11px}
.testimonial .date,.testimonial .author{font-weight:400;color:#333}
.welcome .read-btn{position:static;display:inline-block;margin-top:-2px}

.section-rule{position:absolute;left:160px;top:796px;width:742px;height:1px;background:var(--rule)}

/* services */
.service{position:absolute;top:824px;width:130px;text-align:center}
.service-icon{width:60px;height:60px;margin:0 auto;border-radius:50%;background:#fff;box-shadow:0 1px 3px rgba(0,0,0,.25);padding:5px}
.service-icon span{display:flex;align-items:center;justify-content:center;width:50px;height:50px;border-radius:50%;background:var(--icon-dark)}
.service-title{margin-top:15px;font-size:15px;font-weight:300;color:#333;white-space:nowrap}
.service-photo{position:absolute;top:112px;width:125px;height:54px;border:2px solid #555}
.service-more{position:absolute;top:174px;font-size:11px;font-weight:300;color:#333;white-space:nowrap}

/* footer */
.site-footer{position:absolute;left:0;top:1040px;width:1062px;height:160px;background:var(--footer);border-top:3px double #999}
.footer-col-rule{position:absolute;top:0;width:1px;height:160px;background:var(--footer-rule)}
.footer-links{position:absolute;left:170px;top:43px;font-size:9px;color:var(--footer-text);line-height:17.5px;font-weight:300}
.social{position:absolute;left:170px;top:102px;display:flex;gap:6px}
.social span{width:24px;height:24px;border-radius:2px}
.footer-contact{position:absolute;left:510px;top:27px;font-size:10.5px;color:var(--footer-text);line-height:23.3px;font-weight:300}
.footer-brand{position:absolute;left:730px;top:66px;display:flex;align-items:center;gap:8px}
.footer-brand .brand-mark{background:#6a6a6a}
.footer-brand .brand-name{color:#6a6a6a;font-size:28px}
</style>
</head>
<body>

<header class="site-header">
  <div class="utility-tabs"><span>Contact</span><span>Login</span></div>
  <div class="brand"><div class="brand-mark"></div><div class="brand-name">QUELVO</div></div>
  <nav class="main-nav">
    <span style="left:486px">HOME</span>
    <span style="left:539px">SOLUTIONS</span>
    <span style="left:617px">RESOURCES</span>
    <span style="left:696px">ABOUT</span>
    <span style="left:753px">WHY QUELVO</span>
    <span style="left:837px">CONTACT</span>
  </nav>
  <div class="nav-pointer"></div>
</header>

<section class="hero">
  <h1 class="hero-title">Put Your<br><b>Website</b> on Top<br>of <b>Searchly</b> Seach Engine</h1>
  <p class="hero-copy">Le Lorem Ipsum est simplement du faux texte employé dans la composition et la mise en page avant impression Le Lorem Ipsum est simplement.</p>
  <div class="btn btn-signup">Sign Up for FREE !</div>
  <div class="btn btn-prices">View SEO prices</div>
  <div class="hero-screen"><div class="screen-photo" role="img" aria-label="Video slider showing a smiling doctor with medical staff treating a patient in the background"></div></div>
</section>

<div class="steps-divider"></div>

<div class="step step-teal" style="top:444px">
  <div class="step-number">1</div>
  <div class="step-title">Get Started Today</div>
  <div class="step-sub">Plusieurs variations de Lorem Ipsum.</div>
  <div class="step-text">Le Lorem Ipsum est simplement du faux texte employé dans.</div>
  <div class="read-btn">Read More</div>
</div>
<div class="step-rule" style="top:549px"></div>
<div class="step step-slate" style="top:566px">
  <div class="step-number">2</div>
  <div class="step-title">Build your site</div>
  <div class="step-sub">Plusieurs variations de Lorem Ipsum.</div>
  <div class="step-text">Le Lorem Ipsum est simplement du faux texte.</div>
  <div class="read-btn">Read More</div>
</div>
<div class="step-rule" style="top:669px"></div>
<div class="step step-gold" style="top:687px">
  <div class="step-number">3</div>
  <div class="step-title">Publish &amp; share</div>
  <div class="step-sub">Plusieurs variations de Lorem Ipsum.</div>
  <div class="step-text">Le Lorem Ipsum est simplement du faux texte employé dans la comp.</div>
  <div class="read-btn">Read More</div>
</div>

<section class="welcome">
  <h2>Welcome to QUELVO</h2>
  <p>Contrairement à une opinion répandue, le Lorem Ipsum n'est pas simplement du texte aléatoire. Il trouve ses racines dans une oeuvre de la littérature latine classique datant de 45 av. J.-C., le rendant vieux de 2000 ans.</p>
  <p>Un professeur du Ashbury College, en Virginie, s'est intéressé à un des mots latins les plus obscurs, consectetur, extrait d'un passage du Lorem Ipsum, et en étudiant tous les usages de ce mot dans la littérature classique, découvrit la source incontestable du Lorem Ipsum.</p>
  <p>Contrairement à une opinion répandue, le Lorem Ipsum n'est pas simplement du texte aléatoire. Il trouve ses racines dans une oeuvre de la littérature latine classique datant de 45 av. J.-C., le rendant vieux de 2000 ans.</p>
  <h3>Testimonials</h3>
  <div class="testimonial"><div class="date">1st Jan,&nbsp; 2012</div>Contrairement à une opinion répandue, le Lorem Ipsum n'est pas simplement du texte aléatoire. Il trouve ses racines dans.<div class="author">Martin Hale</div></div>
  <div class="testimonial"><div class="date">1st Jan,&nbsp; 2012</div>Contrairement à une opinion répandue, le Lorem Ipsum n'est pas simplement du texte aléatoire. Il trouve ses racines dans une oeuvre de la littérature latine classique datant de 45 av. J.-C..<div class="author">Martin Hale</div></div>
  <div class="read-btn">Read More</div>
</section>

<div class="section-rule"></div>

<div class="service" style="left:168px">
  <div class="service-icon"><span><svg width="22" height="28" viewBox="0 0 22 28"><rect x="3" y="1" width="16" height="26" rx="2" fill="#fff"/><rect x="6" y="4" width="10" height="7" fill="#333"/><g fill="#333"><rect x="6" y="14" width="2.5" height="2.5"/><rect x="10" y="14" width="2.5" height="2.5"/><rect x="14" y="14" width="2.5" height="2.5"/><rect x="6" y="18" width="2.5" height="2.5"/><rect x="10" y="18" width="2.5" height="2.5"/><rect x="14" y="18" width="2.5" height="2.5"/></g></svg></span></div>
  <div class="service-title">Mobile Website</div>
  <div class="service-photo" style="left:3px;background:linear-gradient(90deg,#0d2f63,#3a6fb5 50%,#0d2f63)" role="img" aria-label="Mobile website screens shown on phones"></div>
  <div class="service-more" style="left:2px">read more ▶</div>
</div>
<div class="service" style="left:371px">
  <div class="service-icon"><span><svg width="24" height="30" viewBox="0 0 24 30"><path d="M12 1C6 1 2 5.5 2 11c0 7 10 18 10 18s10-11 10-18C22 5.5 18 1 12 1z" fill="#fff"/><circle cx="12" cy="11" r="4" fill="#333"/></svg></span></div>
  <div class="service-title" style="margin-top:13px">Maps &amp; Reviews</div>
  <div class="service-photo" style="left:3px;background:linear-gradient(90deg,#6b5040,#c9c2b6 50%,#8a7a6a)" role="img" aria-label="Hand holding a phone showing a map"></div>
  <div class="service-more" style="left:2px">read more ▶</div>
</div>
<div class="service" style="left:573px">
  <div class="service-icon"><span><svg width="30" height="30" viewBox="0 0 30 30" fill="none" stroke="#fff" stroke-width="2.5"><path d="M10 3c-5 2-6 9-2 13s10 2 12-3"/><path d="M20 3c4 3 4 9 0 12"/><path d="M14 16c0 6 2 10 8 10"/><circle cx="9" cy="23" r="3" fill="#fff"/></svg></span></div>
  <div class="service-title">Doctor Portal</div>
  <div class="service-photo" style="left:3px;background:linear-gradient(90deg,#dfe6ed,#f0e8e0 50%,#e3eaf0)" role="img" aria-label="Group of smiling doctors"></div>
  <div class="service-more" style="left:2px">read more ▶</div>
</div>
<div class="service" style="left:752px">
  <div class="service-icon"><span><svg width="26" height="24" viewBox="0 0 26 24"><path d="M3 2h20a2 2 0 0 1 2 2v12a2 2 0 0 1-2 2H11l-6 5v-5H3a2 2 0 0 1-2-2V4a2 2 0 0 1 2-2z" fill="#fff"/></svg></span></div>
  <div class="service-title">Socail Media &amp; Blogs</div>
  <div class="service-photo" style="left:13px;background:linear-gradient(135deg,#f4f1e4,#dfe7ef)" role="img" aria-label="Word cloud about social media and content"></div>
  <div class="service-more" style="left:13px">read more ▶</div>
</div>

<footer class="site-footer">
  <div class="footer-col-rule" style="left:489px"></div>
  <div class="footer-col-rule" style="left:704px"></div>
  <div class="footer-links">
    Home &nbsp;|&nbsp; Solutions &nbsp;|&nbsp; Resources &nbsp;|&nbsp; About &nbsp;|&nbsp; Why Quelvo &nbsp;|&nbsp; Contact<br>
    All content Copyright ©2012 QUELVO<br>
    Terms of Use | Privacy Policy
  </div>
  <div class="social">
    <span style="background:#3b7dc4"></span>
    <span style="background:#1b78b0"></span>
    <span style="background:#d23a2a"></span>
  </div>
  <div class="footer-contact">
    QUELVO, LLC<br>
    Direct - (555) 212 - 0143<br>
    Call - (555) 293 - 0187<br>
    https://www.quelvo.com<br>
    https://www.danverholt.com
  </div>
  <div class="footer-brand"><div class="brand-mark"></div><div class="brand-name">QUELVO</div></div>
</footer>

</body>
</html>
```